Dynamic Business Card for Sports Supplements Company

Hi! I'm looking for an awesome business card to match my existing sports supplement company. I have uploaded my current company logo and screenshot of the front page of my website.

I would like to have something dynamic and interesting and utilize the colors in the website - the reds and purples

The business card should be double sided and focus on a unique eye-catching design on the back and include all the relevant company info.

Most importantly, it should say somewhere: "Sign up on our website for a coupon code."

Target Market(s)

Mostly for women gym goers but it shouldn't be too feminine. It should be in keeping with the website design. It should flow and clearly be connected to it

Industry/Entity Type

Business

Contact Information for Business Card

Lorena K. Vasquez
CEO
LVasquez@Fortivanco.example
www.fortivanco.example
614.275.3081
P.O. Box 48317
Halvern, Ohio 22417

Sign up on our website for a coupon code

Font styles to use
Serif
Sans Serif
Other font styles liked:
• Novecento font family and "Fortivan" is in AR Destine font

Requirements
Must have
• One side should be a bold Fortivan logo design. Even just the symbol itself may be o.k. (see attached file)

```html
<!DOCTYPE html>
<html lang="en">
<head>
<meta charset="utf-8">
<title>Fortivan Business Card</title>
<link href="https://fonts.googleapis.com/css2?family=Lato:wght@400;700;900&display=swap" rel="stylesheet">
<style>
  :root {
    --purple: #7e2a8e;
    --purple-deep: #5f1d6d;
    --purple-light: #b486c0;
    --ink: #1f1f1f;
    --paper: #f7f7f7;
    --stage: #2b2b2b;
    --grey-text: #3a3a3a;
  }
  * { margin: 0; padding: 0; box-sizing: border-box; }
  html, body { width: 1200px; height: 834px; overflow: hidden; }
  body {
    background: var(--stage);
    font-family: "Lato", sans-serif;
    position: relative;
  }
  .card {
    position: absolute;
    width: 560px;
    height: 320px;
    overflow: hidden;
    box-shadow: 0 14px 30px rgba(0,0,0,0.45);
  }
  /* Front side */
  .card-front {
    left: 50px; top: 90px;
    background: radial-gradient(ellipse at 50% 60%, #8a2f9c 0%, var(--purple) 50%, var(--purple-deep) 100%);
  }
  .card-front .wordmark {
    position: absolute;
    top: 92px; left: 0; width: 100%;
    text-align: center;
    font-weight: 900;
    font-size: 46px;
    letter-spacing: 3px;
    color: #ffffff;
  }
  .card-front .coupon-band {
    position: absolute;
    left: 0; top: 196px;
    width: 100%; height: 46px;
    background: linear-gradient(#ffffff, #e6e6e6);
    display: flex; align-items: center; justify-content: center;
    font-size: 14px;
    color: var(--grey-text);
  }
  /* Back side */
  .card-back {
    left: 590px; top: 424px;
    background: linear-gradient(160deg, #ffffff 0%, #ececec 100%);
  }
  .card-back .chevron { position: absolute; left: 0; top: 0; }
  .card-back .wordmark {
    position: absolute;
    top: 62px; left: 0; width: 100%;
    text-align: center;
    font-weight: 900;
    font-size: 38px;
    letter-spacing: 3px;
    color: var(--ink);
  }
  .holder {
    position: absolute;
    left: 40px; top: 232px;
    color: #ffffff;
  }
  .holder .name { font-size: 18px; font-weight: 700; }
  .holder .role { font-size: 13px; margin-top: 4px; }
  .contact {
    position: absolute;
    left: 330px; top: 206px;
    color: #ffffff;
    font-size: 12.5px;
    line-height: 17px;
    list-style: none;
  }
  .contact li { display: flex; align-items: center; gap: 8px; }
  .contact .icon { width: 12px; height: 12px; flex: none; }
</style>
</head>
<body>

<section class="card card-front" aria-label="Card front">
  <div class="wordmark">FORTIVAN</div>
  <div class="coupon-band">Sign up on our website for a coupon code</div>
</section>

<section class="card card-back" aria-label="Card back">
  <svg class="chevron" width="560" height="320" viewBox="0 0 560 320" aria-hidden="true">
    <defs>
      <linearGradient id="backPurple" x1="0" y1="0" x2="1" y2="1">
        <stop offset="0" stop-color="#8a2f9c"/>
        <stop offset="1" stop-color="#5f1d6d"/>
      </linearGradient>
    </defs>
    <polygon points="0,150 300,185 560,125 560,133 300,193 0,158" fill="#d9c3de"/>
    <polygon points="0,158 300,193 560,133 560,320 0,320" fill="url(#backPurple)"/>
    <polyline points="0,156 300,191 560,131" fill="none" stroke="#a86bb6" stroke-width="2"/>
  </svg>
  <div class="wordmark">FORTIVAN</div>

  <div class="holder">
    <div class="name">Lorena K. Vasquez</div>
    <div class="role">CEO</div>
  </div>

  <ul class="contact">
    <li>P.O. Box 48317</li>
    <li>Halvern, Ohio 22417</li>
    <li>
      <svg class="icon" viewBox="0 0 12 12"><path d="M2.5 1 4.5 1 5.3 3.5 4 4.5Q5 7 7.5 8L8.5 6.7 11 7.5 11 9.5Q11 11 9.5 11 1 10 1 2.5 1 1 2.5 1Z" fill="none" stroke="#fff" stroke-width="1"/></svg>
      614.275.3081
    </li>
    <li>
      <svg class="icon" viewBox="0 0 12 12"><rect x="1" y="2.5" width="10" height="7" fill="none" stroke="#fff" stroke-width="1"/><path d="M1 2.5 6 6.5 11 2.5" fill="none" stroke="#fff" stroke-width="1"/></svg>
      LVasquez@Fortivanco.example
    </li>
    <li>
      <svg class="icon" viewBox="0 0 12 12"><circle cx="6" cy="6" r="5" fill="none" stroke="#fff" stroke-width="1"/><ellipse cx="6" cy="6" rx="2.2" ry="5" fill="none" stroke="#fff" stroke-width="0.8"/><path d="M1 6H11" stroke="#fff" stroke-width="0.8"/></svg>
      www.fortivanco.example
    </li>
  </ul>
</section>

</body>
</html>
```